Digital Imaging Website Design Project

This project is for 3 page designs - The main Home page design, department page design & content page design which will utilize most of the home page components.

Client Background - http://www.kelvarprint.example

An almost Forty year old established printing company that has a large client base of architect/engineering, as the print shop opened up as a blueprinting company, and over the years has grown, changed and expanded to offer document and digital file management for this industry. KPRInc. has also always offered color printing services, but recently has expanded their color department to be able to offer amazing dimensional printing, and extreme cutting technology.

These new products and services will be targeted to new industries for repeatable printing needs, promotional, point of purchase color printing, as well as in-store, interior decor/wall. These new printing services are only offered by KPRINC in their area, and they want to convey that they are on the leading edge of color printing technology, while at the same time, not eliminating their existing primary business scaring away their traditional client base of architectural/engineering firms that use them for large format printing, scanning and document management services.

1 - Home Page Design
Primary Goals of the design:

1.Provide a new, eye catching engaging website that conveys the above expansion/growth/cutting edge company.
2.Full screen design please to move away from the 'center' bordered up website they currently have.
3.Design Components – We don't have any media to provide you with exception of our logo. We're looking for fresh design that is exciting and engaging imagery. Additionally, we are working on a color/effected version of our logo to place on the color division page, and this will probably tie in with the design you create for us.
4.It should be designed to be able to work as a responsive design as well so that when installed, will work across devices etc..
5.Colors – Same color scheme, but if you have an accent color you'd like to use to make the site pop, go for it!

Requirements:
1.The 4 divisions of the company should be the main feature so that the client depending on which department they are needing, will see those 4 choices clearly in the design, and they'll know to click on one of them to get more information and to their needed services.

2.The main goal of the site is to get visitors to place an order, there should be a feature on the home page for this call to action.

3.Put in an element that communicates the main benefit of KPRInc. - an area for a 1-line Statement/Call to Action / Overall Company Benefit/

4.The 4 divisions need to have eye catching elements related to their products and services, and that clearly illustrate that the user should click on that to go to the appropriate area for products and services

Reprographics
This department is specifically geared to architect/engineering industry
BYLine for optional Use: Partnering with Building Industry Providers since 1975
Related pages for better understanding:
http://www.kelvarprint.example/services/portland_professional_printing_services
http://www.kelvarprint.example/services/reprographics
Digital File Management
This department is related to Architect/engineers, but can also apply to any other industry needing electronic document management, scanning, or archival services.
BYLine for optional use: Effective & Efficient Digital Solutions at every level.
Related Pages:
http://www.kelvarprint.example/colorgraphics/electronic_file_document_management
http://www.kelvarprint.example/colorgraphics/document_scanning_service
http://www.kelvarprint.example/services/scanning_and_archiving

Color Graphics
This Department is newly expanded / has expanded services / they are focusing more of their efforts on this department and is a key reason for updated website design.
This Department image/representation should be stellar in the imagery to convey the excellence of the color department the services availble.
One of their newest products/services is dimensional printing – not 3-D, but raised element printing. Essentially a client could pick components on their graphic that that they want to 'bump' out, and additional layers would be put in place to create a popped out, dimensional effect. * Bonus points for creating the color department image that effectively conveys this new service – whether it's showing an abstract image/element that is actually raised off the page/paper/component. Additionally the color dimensional printing can be done on practically any material – glass, vinyl, material etc.... Please let me know if you have any questions on this.
BYLine for optional Use: See How Our Color Stands Out From the Rest
Related pages:
http://www.kelvarprint.example/colorgraphics
http://www.kelvarprint.example/colorgraphics/color_digital_imaging

Equipment & Supplies
This department provides specific supplies and hardware vs. printing products/services. Our largest client base is architects/engineers, but is not limited to this industry. Typical equipment is large printers, and supplies are typically paper products geared to the large format printing services, for the architect/engineers industry.
Byline for optional Use: In-House Printing & Fulfillment Services
Related pages:
http://www.kelvarprint.example/tervik_amlo_equipment_sales
http://www.kelvarprint.example/supplies

Additionally - Possibly have descriptive text sections below these 4 elements, but this is optional.

2.) Department/Division Page design -

This page should pull the home page element to over based on which division is selected.
Have a submenu design incorporated so that users can navigate to all the products and services that will be listed under that division
Contain a plugin design for FAQs – so that depending on which division page they are on, the appropriate FAQ's would display for use to have easy access to.
Contain a plugin design for – Contact Us easy form – short form –
Name
Company
Number
Email
Project Details/Questions: Text box

3.)Content Page design
This page should have main area for content
Area for an image with slideshow of other supporting images
Optional area for video – most (99%) of the pages will not have videos, but in the case we do, would like an area that will display videos effectively.
Optional FAQ plugin display
Contact plugin display

Global Elements:

Static and very visible site features that are in a position so that if user clicks beyond home page will still see these are:
Get a Quote
Place Order
Digital Plan-room
Call Today - 541-867-2290

Other global components:
SM Icons – QX, Chirply, ProNexa
Rotating Testimonial

Navigational Menu:
The KPR Difference
About
Sustainability
Products & Services
Reprograhics
Digital File Management
Color Graphics
Equipment & Supplies
Login
Blog
Contact Us

After the contest – What would be great to have is when a user clicks on one of the departments, it takes that visual element and continues onto it's department page for a smaller but related image - But this may be an after this web design contest.

Additionally will need some other design work on the interior pages, as well, so hoping to find a great designer to complete the other tasks – as well as be the go-to for future endeavors!

Thanks for looking at the project, and I look forward to any questions you may have.

Looking forward to hearing from interested designers! - If you're curious about my work, you can find my profile at:  https://www.freelanzo.example/users/~07b3e2c91f4d6a05

Please see description

```html
<!DOCTYPE html>
<html lang="en">
<head>
<meta charset="utf-8">
<title>KPR Digital Imaging</title>
<link rel="stylesheet" href="https://fonts.googleapis.com/css2?family=Open+Sans:wght@300;400;600;700&family=Oswald:wght@400;500&family=Roboto+Condensed:wght@400&family=Libre+Baskerville:wght@400;700&display=swap">
<style>
:root{
  --navy:#27297a;
  --navy-dark:#222266;
  --footer:#2e2f84;
  --red:#c4161c;
  --ink:#3a3a3a;
  --muted:#666;
  --grey-bar:#e4e4e4;
  --page:#f4f4f4;
  --panel:#e2e2e2;
  --white:#fff;
}
*{margin:0;padding:0;box-sizing:border-box}
html,body{width:838px;height:1200px;overflow:hidden;background:var(--page)}
body{font-family:"Open Sans",sans-serif;color:var(--ink)}
.site{position:relative;width:980px;height:1403px;transform:scale(.8551);transform-origin:0 0;background:var(--page)}
.abs{position:absolute}
a{color:inherit;text-decoration:none}

/* header */
.header{left:0;top:0;width:980px;height:68px;background:linear-gradient(#fff,#ececec);border-bottom:1px solid #ddd}
.brand{left:140px;top:14px;display:flex;align-items:center;gap:8px;color:var(--navy);font-weight:700}
.brand-mark{width:14px;height:14px;background:var(--navy)}
.brand-name{font-size:24px;letter-spacing:1px}
.brand-sub{font-size:9px;line-height:11px;font-weight:700;text-transform:uppercase;width:120px}
.nav{left:563px;top:29px;display:flex;gap:14px;font-family:"Roboto Condensed",sans-serif;font-size:13px;color:#777}
.nav .active{color:var(--navy)}
.quote-btn{left:748px;top:25px;width:92px;height:22px;background:var(--navy);color:#fff;font-family:"Libre Baskerville",serif;font-size:12px;text-align:center;line-height:22px;border-bottom:2px solid #6a6cc0}

/* hero */
.hero{left:0;top:68px;width:980px;height:341px;background:
 radial-gradient(ellipse at 50% 40%,rgba(255,255,255,.55),rgba(255,255,255,0) 55%),
 linear-gradient(100deg,#1d2f6a 0%,#3f7d8a 12%,#5c9c6a 24%,#8aa860 34%,#b4a6c0 46%,#d8c2d0 54%,#c86a8a 64%,#d0a860 76%,#5c8a9a 88%,#162058 100%)}
.hero-arrow{top:226px}
.hero-title{left:337px;top:200px;width:306px;height:40px;background:var(--navy);color:#fff;font-weight:300;font-size:25px;text-align:center;line-height:40px}
.hero-sub{left:239px;top:241px;width:502px;height:34px;background:var(--navy);color:#fff;font-size:18px;text-align:center;line-height:34px}
.hero-cta{left:404px;top:277px;width:173px;height:38px;background:var(--red);color:#fff;font-family:"Oswald",sans-serif;font-size:23px;font-weight:500;text-align:center;line-height:38px;border-bottom:2px solid #8d0e12}

/* call bar */
.callbar{left:0;top:409px;width:980px;height:50px;background:var(--grey-bar)}
.call{left:145px;top:419px;display:flex;align-items:center;gap:8px;font-size:18px;color:#333}
.call strong{font-weight:600}
.planroom{left:640px;top:409px;width:167px;height:50px;background:var(--navy);color:#fff;font-family:"Oswald",sans-serif;font-size:20px;line-height:50px;padding-left:10px}
.planroom-go{left:807px;top:409px;width:33px;height:50px;background:var(--red)}

/* welcome */
.welcome-title{left:140px;top:511px;font-size:18px;color:#888;font-weight:400}
.welcome-title b{color:var(--navy);font-weight:600}
.welcome-text{left:140px;top:548px;width:474px;font-size:11px;line-height:15px;color:#555}
.rule{left:142px;top:629px;width:400px;border-top:3px dotted #ccc}
.welcome-more{left:549px;top:621px;font-size:11.5px;color:#444}

/* divisions */
.division{width:220px}
.division h3{font-size:14.5px;font-weight:600;color:var(--navy);line-height:18px}
.division .byline{font-size:10.5px;color:#555;line-height:13px;height:33px;margin-top:1px}
.division .visual{height:101px;margin-top:13px}
.division p{font-size:8.5px;line-height:13.5px;color:#666;margin-top:15px;height:52px}
.division .more{display:block;font-size:9px;font-weight:700;color:var(--navy);margin-top:13px}
.row-rule{left:388px;top:926px;width:219px;border-top:1px solid #ddd}

/* sidebar */
.side-menu{left:641px;top:514px;width:199px;height:246px;background:linear-gradient(90deg,#dcdcdc,#ececec 70%,#dedede);border-radius:2px}
.side-menu li{list-style:none;height:22px;line-height:22px;padding-left:12px;font-size:11px;color:#333;border-bottom:1px solid #f8f8f8}
.order-btn{left:641px;top:773px;width:199px;height:31px;background:var(--navy);color:#fff;font-family:"Libre Baskerville",serif;font-size:20px;text-align:center;line-height:31px;border-bottom:2px solid #7a7cd0}
.follow{left:641px;top:829px;width:199px;text-align:center;font-size:14px;color:#333}
.social{left:681px;top:853px;display:flex;gap:3px}
.social span{width:21px;height:21px;display:block}
.testimonials{left:641px;top:900px;width:199px;height:173px;background:linear-gradient(#d9d9d9,#e8e8e8);padding:14px 13px}
.testimonials h4{font-size:15px;font-weight:400;color:var(--navy)}
.testimonials p{font-size:10px;line-height:12px;color:#666;margin-top:8px}
.testimonials .who{font-size:10px;font-weight:600;color:#555;margin-top:12px;padding-left:3px}
.testimonials .role{font-size:8.5px;color:#666;padding-left:3px}

/* footer */
.footer-gap{left:0;top:1228px;width:980px;height:12px;background:#e6e6e6}
.footer{left:0;top:1240px;width:980px;height:128px;background:var(--footer);color:#e8e8f6;font-size:9px}
.footer ul{position:absolute;top:25px;list-style:none;line-height:16.3px}
.footer .social-list li{display:flex;align-items:center;gap:5px}
.footer .social-list i{width:8px;height:8px;border-radius:50%;background:#e8e8f6;display:block}
.footer p{position:absolute;left:661px;top:25px;width:180px;line-height:13.5px;font-size:8.5px}
.legal{left:0;top:1368px;width:980px;height:35px;background:var(--navy-dark);color:#ddd;font-size:8.5px;text-align:center;line-height:37px}
</style>
</head>
<body>
<div class="site">

  <header class="header abs"></header>
  <div class="brand abs">
    <span class="brand-mark"></span>
    <span class="brand-name">KPR</span>
    <span class="brand-sub">Kelvar Print &amp; Reprographics Co.</span>
  </div>
  <nav class="nav abs"><a class="active">HOME</a><a>DEPARTMENT</a><a>CONTENT</a></nav>
  <a class="quote-btn abs">Get A Quote</a>

  <section class="hero abs" role="img" aria-label="Architectural blueprint floor plan washed with rainbow colour bands"></section>
  <svg class="hero-arrow abs" style="left:38px" width="24" height="34" viewBox="0 0 24 34"><path d="M20 3 6 17l14 14" fill="none" stroke="#c9c9c9" stroke-width="6"/></svg>
  <svg class="hero-arrow abs" style="left:908px" width="24" height="34" viewBox="0 0 24 34"><path d="M4 3l14 14L4 31" fill="none" stroke="#c9c9c9" stroke-width="6"/></svg>
  <h1 class="hero-title abs">Lorem Ipsum Dolor Sit Amet</h1>
  <div class="hero-sub abs">Vestibulum vehicula posuere hendrerit. Fusce sagittis nunc id</div>
  <a class="hero-cta abs">ORDER NOW</a>

  <div class="callbar abs"></div>
  <div class="call abs">
    <svg width="30" height="30" viewBox="0 0 30 30"><circle cx="15" cy="15" r="15" fill="#6b6b6b"/><path d="M10 8c1-1 2-1 3 0l1.5 2.5c.5 1 0 1.7-.8 2.3-.5.4-.4 1 0 1.7 1 1.6 2 2.6 3.5 3.5.7.4 1.3.5 1.7 0 .6-.8 1.3-1.3 2.3-.8L23.7 18c1 1 1 2 0 3-2 2-4.5 2-8-1-3.5-3-6.5-7-5.7-12z" fill="#fff"/></svg>
    <span>Call Us Today - <strong>541-867-2290</strong></span>
  </div>
  <a class="planroom abs">Digital Plan-room</a>
  <div class="planroom-go abs"><svg width="33" height="50" viewBox="0 0 33 50"><path d="M11 13l12 12-12 12" fill="none" stroke="#fff" stroke-width="2"/></svg></div>

  <h2 class="welcome-title abs">Welcome to <b>Kelvar Print &amp; Reprographics Company, INC.</b></h2>
  <p class="welcome-text abs">Aenean dapibus lorem laoreet ante pharetra ornare malesuada orci ornare. Ut volutpat ipsum ipsum, eget suscipit mauris. Sed sed nisl ac justo rutrum convallis. Fusce facilisis, nunc et viverra iaculis, arcu augue tempor ipsum, ut auctor sapien justo ac metus. Morbi adipiscing sodales condi-mentum. Nunc porta hendrerit turpis, nec pharetra enim interdum id.</p>
  <div class="rule abs"></div>
  <a class="welcome-more abs">Read More</a>

  <article class="division abs" style="left:140px;top:663px">
    <h3>Reprographics</h3>
    <div class="byline">Partnering with Building Industry Providers since 1975</div>
    <div class="visual" role="img" aria-label="Blueprint with drafting compass, scale ruler and model house" style="background:linear-gradient(135deg,#2d4f8e,#6f8fbf 50%,#24427a)"></div>
    <p>Aenean dapibus lorem laoreet ante pharetra ornare malesuada orci ornare. Ut volutpat ipsum ipsum, eget suscipit mauris. Sed sed nisl ac justo rutrum convallis. Fusce facilisis, nunc et viverra iaculis,</p>
    <a class="more">Read More</a>
  </article>
  <article class="division abs" style="left:388px;top:663px">
    <h3>Digital File Management</h3>
    <div class="byline">Effective &amp; Efficient Digital Solutions at every level</div>
    <div class="visual" role="img" aria-label="Colour print proofs with loupe and colour swatches" style="background:linear-gradient(135deg,#c8242c,#e8b070 45%,#4a7ab8 80%,#d84a8a)"></div>
    <p>Aenean dapibus lorem laoreet ante pharetra ornare malesuada orci ornare. Ut volutpat ipsum ipsum, eget suscipit mauris. Sed sed nisl ac justo rutrum convallis. Fusce facilisis, nunc et viverra iaculis,</p>
    <a class="more">Read More</a>
  </article>
  <div class="row-rule abs"></div>
  <article class="division abs" style="left:140px;top:940px">
    <h3>Color Graphics</h3>
    <div class="byline">See How Our Color Stands Out From the Rest Related pages</div>
    <div class="visual" role="img" aria-label="Raised rainbow colour waves" style="background:linear-gradient(160deg,#e3262e,#f07a1e 25%,#f6d21c 50%,#7cc242 72%,#3aa8e0)"></div>
    <p>Aenean dapibus lorem laoreet ante pharetra ornare malesuada orci ornare. Ut volutpat ipsum ipsum, eget suscipit mauris. Sed sed nisl ac justo rutrum convallis. Fusce facilisis, nunc et viverra iaculis,</p>
    <a class="more">Read More</a>
  </article>
  <article class="division abs" style="left:388px;top:940px">
    <h3>Equipment &amp; Supplies</h3>
    <div class="byline">In-House Printing &amp; Fulfillment Services</div>
    <div class="visual" role="img" aria-label="Large format printing press in a print shop" style="background:linear-gradient(90deg,#5a5a5a,#8a8a8a 50%,#4a4a4a)"></div>
    <p>Aenean dapibus lorem laoreet ante pharetra ornare malesuada orci ornare. Ut volutpat ipsum ipsum, eget suscipit mauris. Sed sed nisl ac justo rutrum convallis. Fusce facilisis, nunc et viverra iaculis,</p>
    <a class="more">Read More</a>
  </article>

  <ul class="side-menu abs" style="padding-top:3px">
    <li>The KPR Difference</li><li>About</li><li>Sustainability</li><li>Products &amp; Services</li><li>Reprograhics</li><li>Digital File Management</li><li>Color Graphics</li><li>Equipment &amp; Supplies</li><li>Login</li><li>Blog</li><li>Contact Us</li>
  </ul>
  <a class="order-btn abs">Order Now</a>
  <div class="follow abs">Follow Us On</div>
  <div class="social abs" aria-label="Social links">
    <span style="background:#3b5998"></span><span style="background:#3aa7e0"></span><span style="background:#d8322a"></span><span style="background:#1a7bb8"></span><span style="background:#c4161c"></span>
  </div>
  <aside class="testimonials abs">
    <h4>Testimonials</h4>
    <p>Phasellus tellus augue, laoreet sit amet semper eu, dignissim nec felis. Aenean iaculis risus a erat dictum venenatis. Pellentesque convallis fringilla est, at laoreet orci ullamcorper non. Cum sociis</p>
    <div class="who">Phasellus ut libero ut</div>
    <div class="role">nulla mattis rutrum a non augue</div>
  </aside>

  <div class="footer-gap abs"></div>
  <footer class="footer abs">
    <ul style="left:140px"><li>Home</li><li>Department</li><li>Content</li></ul>
    <ul style="left:248px"><li>The KPR Difference</li><li>About</li><li>Sustainability</li><li>Products &amp; Services</li><li>Reprograhics</li></ul>
    <ul style="left:391px"><li>Digital File Management</li><li>Color Graphics</li><li>Equipment &amp; Supplies</li><li>Login</li><li>Blog</li></ul>
    <ul class="social-list" style="left:552px"><li><i></i>QX</li><li><i></i>Chirply</li><li><i></i>Orbitly</li><li><i></i>ProNexa</li><li><i></i>Streamora</li></ul>
    <p>Ut volutpat ipsum ipsum, eget suscipit mauris. Sed sed nisl ac justo rutrum convallis. Fusce facilisis, nunc et viverra iaculis, arcu augue tempor ipsum, ut auctor sapien justo ac metus. Morbi adipiscing</p>
  </footer>
  <div class="legal abs">© Copyright 2013. All Rights Reserved.</div>

</div>
</body>
</html>
```